BEACON traffic management plans

The preparation of traffic management plans for architects, builders, landscapers for council approval. The preparation of the plans can include submitting to council, briefing the builder regarding management of the plan, onsite visit, taking photographs, measurements and establishing the best outcome. Implementing the plan can also take place if need be.
NO EXISTING LOGO AVAILABLE
No photos or documents available to upload

Target Market(s)

Builders, architects, landscapers
No existing logo availalble

Industry/Entity Type

Builders

Contact Information for Business Card

BEACON Traffic Management Plans
Tom Ridgway
harbourlane@westnetmail.com.au
0427 615 938

Font styles to use
Serif

Colors
1b1b1b

Requirements
Must have
• competitive prices
• No existing logo available
• No photos available
Nice to have
• Black with orange and white
• No existing logo available no
Should not have
• no existing logo available
• No photos or documents to upload

```html
<!DOCTYPE html>
<html lang="en">
<head>
<meta charset="utf-8">
<title>BEACON Traffic Management Plans – Business Card</title>
<link rel="stylesheet" href="https://fonts.googleapis.com/css2?family=Open+Sans:wght@400;600&display=swap">
<style>
  :root {
    --page-bg: #e9e7e4;
    --card-black: #1b1b1b;
    --brand-orange: #f2650b;
    --divider-grey: #a9a9a9;
    --wordmark-grey: #c4c4c4;
    --text-white: #ffffff;
  }
  * { margin: 0; padding: 0; box-sizing: border-box; }
  html, body {
    width: 1200px;
    height: 900px;
    overflow: hidden;
    background: var(--page-bg);
    font-family: "Open Sans", Arial, sans-serif;
  }
  .business-card {
    position: absolute;
    left: 150px;
    top: 172px;
    width: 900px;
    height: 555px;
    background: var(--card-black);
    overflow: hidden;
    box-shadow: 0 10px 30px rgba(0,0,0,0.18);
  }
  .contact-band {
    position: absolute;
    left: 0;
    right: 0;
    bottom: 0;
    height: 210px;
    background: var(--brand-orange);
    border-top: 8px solid var(--divider-grey);
  }
  .brand-name {
    position: absolute;
    left: 66px;
    top: 200px;
    display: flex;
    align-items: center;
    gap: 16px;
  }
  .brand-square {
    width: 26px;
    height: 26px;
    background: var(--brand-orange);
    flex: none;
  }
  .brand-text {
    color: var(--wordmark-grey);
    font-size: 34px;
    font-weight: 400;
    line-height: 1.2;
    white-space: nowrap;
  }
  .contact-block {
    position: absolute;
    right: 53px;
    top: 378px;
    text-align: right;
    color: var(--text-white);
  }
  .contact-name {
    font-size: 29px;
    font-weight: 600;
    line-height: 1.2;
    margin-bottom: 28px;
  }
  .contact-line {
    display: flex;
    justify-content: flex-end;
    align-items: center;
    gap: 10px;
    font-size: 22px;
    font-weight: 400;
    line-height: 36px;
  }
  .contact-icon {
    width: 18px;
    height: 18px;
    fill: var(--text-white);
    flex: none;
  }
</style>
</head>
<body>
  <div class="business-card">
    <div class="contact-band"></div>

    <div class="brand-name">
      <span class="brand-square"></span>
      <span class="brand-text">BEACON Traffic Management Plans</span>
    </div>

    <div class="contact-block">
      <p class="contact-name">Tom Ridgway</p>
      <p class="contact-line">
        <span>0427 615 938</span>
        <svg class="contact-icon" viewBox="0 0 24 24" aria-hidden="true"><path d="M6.6 10.8a15.1 15.1 0 0 0 6.6 6.6l2.2-2.2c.3-.3.7-.4 1-.2 1.1.4 2.3.6 3.6.6.6 0 1 .4 1 1V20c0 .6-.4 1-1 1C10.6 21 3 13.4 3 4c0-.6.4-1 1-1h3.5c.6 0 1 .4 1 1 0 1.3.2 2.5.6 3.6.1.3 0 .7-.2 1z"/></svg>
      </p>
      <p class="contact-line">
        <span>harbourlane@westnetmail.com.au</span>
        <svg class="contact-icon" viewBox="0 0 24 24" aria-hidden="true"><path d="M2 5h20v14H2z M4 7v.4l8 5.2 8-5.2V7z" fill-rule="evenodd"/></svg>
      </p>
    </div>
  </div>
</body>
</html>
```